Lumora Learning Web Design Project

Who We are:
Lumora Learning is education information portal/ magazine, providing information about the Chinese and International education markets. Our aim is to help school principals improve there curriculum, and parents in understanding this curriculum.

Project Brief:
The site will include education news updates, educational services, curriculum developments and overseas study. We hope the site represents the cross cultural bridge between the west and east. The site will cover both the Sciences and Arts.

Note:
The logo design competition is also underway so we only need the website design

What We want:
This competition is for Design only no coding!
Design a home page based on Template 1,2 or 3. I only need to select one.
The design of an article page.

Optional
Design a Microsoft Windows metro style splash page.

Sites We like:
http://www.kavelin.com.cn/kavelinlingo/default.aspx
http://www.brixtalacademia.co.uk/
http://qrpv.norvatestudio.net/

Template Explanations:
Template 1-
The main information has a dynamic sliding category view that when clicked displays the relevant info.
In addition to the main upper menu it also has a left hand sliding menu that pops out on click or gesture

Template 2-
Has limited number of Articles most of the menus are drop downs from the top menu

Template 3-
No Top menu

Target Market(s)

Teachers, principals and parents

Industry/Entity Type

Education

Requirements
Should not have
• kindergarten preschool feel

```html
<!DOCTYPE html>
<html lang="en">
<head>
<meta charset="utf-8">
<title>Lumora Learning</title>
<link href="https://fonts.googleapis.com/css2?family=Mulish:wght@300;400;600;700&display=swap" rel="stylesheet">
<style>
:root{
  --navy:#1d4c8c;
  --navy-dark:#173f78;
  --orange:#ef8e1c;
  --green:#2f9e46;
  --red:#e0423f;
  --purple:#5a2c7d;
  --sky:#2c90c6;
  --white:#ffffff;
  --text:#666a70;
  --line:#e6e6e6;
}
*{box-sizing:border-box;margin:0;padding:0}
html,body{width:1200px;height:1066px;overflow:hidden}
body{
  position:relative;
  font-family:"Mulish",Arial,sans-serif;
  color:var(--text);
  background:
    linear-gradient(180deg,
      #2a6fc4 0%,#4a97dc 18%,#6fc0ea 38%,#45c9d6 58%,#3ab7b8 70%,
      #101418 81%,#1b2a2c 86%,#7fd36a 92%,#f0a24a 96%,#d87be0 100%);
}
.abs{position:absolute}
.logo{left:196px;top:16px;width:170px;height:96px}
.logo-mark{position:absolute;left:50px;top:0;width:52px;height:52px;border-radius:50%;background:var(--red)}
.logo-name{position:absolute;left:0;top:60px;font-weight:700;font-size:17px;color:var(--navy);letter-spacing:.2px;white-space:nowrap}
.search{left:790px;top:78px;width:206px;height:28px;background:var(--white);border:1px solid #d6d6d6;font-size:12px;color:#999;padding:8px 9px;letter-spacing:.3px}
.search svg{position:absolute;right:6px;top:5px}
.nav{left:195px;top:116px;width:801px;height:39px;background:var(--white);display:flex}
.nav a{display:block;height:39px;line-height:36px;font-size:12.5px;color:#d2352f;text-decoration:none;text-align:center;border-bottom:3px solid;border-right:1px solid #ececec}
.nav a.active{background:var(--navy);color:var(--white)}
.side{left:195px;top:164px;width:60px}
.side-tile{height:72px;color:var(--white);font-size:8.5px;font-weight:700;text-align:center;padding-top:13px}
.side-tile svg{display:block;margin:0 auto 6px}
.social{left:195px;top:679px;width:60px}
.social div{height:60px}
.hero{left:263px;top:164px;width:537px;height:236px;display:flex}
.hero-text{width:243px;background:var(--navy);color:var(--white);padding:50px 14px 0}
.hero-text h1{font-weight:300;font-size:20px;line-height:17.5px;letter-spacing:.2px}
.hero-text p{font-size:10px;line-height:13.6px;margin-top:10px;color:#dfe8f3}
.more{font-size:14px;font-weight:300;margin-top:10px;display:flex;align-items:center;gap:4px;color:var(--white)}
.hero-photo{flex:1;background:linear-gradient(120deg,#4a4c4c,#6d6f6e 55%,#e7e5e3)}
.cat-head{left:263px;top:409px;width:537px;height:44px;background:var(--navy);color:var(--white);font-weight:300;font-size:22px;padding:9px 14px}
.cat-body{left:263px;top:453px;width:537px;height:199px;background:var(--white)}
.card{display:flex;padding:8px;color:var(--white)}
.card-photo{width:96px;height:70px;flex:none}
.card-text{padding-left:10px;font-size:11.5px;font-weight:700;line-height:13.6px}
.card-text .more{font-size:14px;margin-top:4px}
.feature{left:536px;top:462px;width:256px;height:180px;background:var(--green);padding:8px 7px;color:var(--white)}
.feature-photo{height:135px;background:linear-gradient(110deg,#c49a6a,#e9d6b8 50%,#b87344)}
.feature p{font-size:11.5px;font-weight:700;line-height:13.6px;margin-top:4px}
.bar{height:44px;color:var(--white);font-weight:300;font-size:22px;padding:8px 11px}
.col-l{left:263px;top:652px;width:264px}
.col-r{left:536px;top:652px;width:264px}
.panel-head{height:44px;color:var(--white);font-weight:300;font-size:23px;padding:8px 11px}
.list{background:var(--white)}
.list li{list-style:none;height:49px;border-bottom:1px solid var(--line);border-left:3px solid;font-size:11.5px;line-height:15.5px;padding:8px 9px;color:var(--text)}
.articles{left:808px;top:164px;width:188px}
.blogposts{left:808px;top:513px;width:188px;height:315px;overflow:hidden}
.footer{left:263px;top:836px;width:733px;height:146px;background:var(--white);display:flex}
.fcol{border-bottom:5px solid;border-right:1px solid var(--line);padding:20px 0 0 40px}
.fcol h3{font-size:15px;font-weight:700;margin-bottom:6px}
.fcol li{list-style:none;font-size:10.5px;line-height:15.7px;color:var(--text)}
.copy{left:263px;top:990px;width:733px;height:48px;background:var(--navy);color:var(--white);font-size:10.5px;text-align:center;line-height:48px}
</style>
</head>
<body>

<div class="abs logo">
  <div class="logo-mark"></div>
  <div class="logo-name">LUMORA LEARNING</div>
</div>

<div class="abs search">SEARCH
  <svg width="18" height="18" viewBox="0 0 18 18"><circle cx="7" cy="7" r="5.5" fill="none" stroke="#999" stroke-width="2"/><line x1="11" y1="11" x2="16.5" y2="16.5" stroke="#999" stroke-width="2.5"/></svg>
</div>

<nav class="abs nav">
  <a class="active" style="width:71px;border-color:var(--navy-dark)">HOME</a>
  <a style="width:96px;border-color:var(--orange)">ABOUT US</a>
  <a style="width:128px;border-color:var(--green)">FOR STUDENTS</a>
  <a style="width:82px;border-color:var(--red)">LESSON</a>
  <a style="width:67px;border-color:var(--purple)">BLOG</a>
  <a style="width:82px;border-color:var(--sky)">JOIN US</a>
  <a style="width:95px;border-color:var(--green)">CONTACT</a>
  <a style="flex:1;border-color:#e8c21c;border-right:0"></a>
</nav>

<div class="abs side">
  <div class="side-tile" style="background:var(--navy)">
    <svg width="22" height="22" viewBox="0 0 22 22"><path d="M11 2 2 11h3v9h5v-6h2v6h5v-9h3z" fill="#fff"/></svg>HOME</div>
  <div class="side-tile" style="background:var(--orange)">
    <svg width="22" height="22" viewBox="0 0 22 22"><circle cx="11" cy="11" r="10" fill="#fff"/><rect x="9.7" y="9" width="2.6" height="8" fill="var(--orange)"/><circle cx="11" cy="6" r="1.6" fill="var(--orange)"/></svg>ABOUT US</div>
  <div class="side-tile" style="background:var(--green)">
    <svg width="28" height="22" viewBox="0 0 28 22"><path d="M14 3 1 9l13 6 13-6z" fill="#fff"/><path d="M6 12v5c4 3 12 3 16 0v-5l-8 4z" fill="#fff"/></svg>STUDENTS</div>
  <div class="side-tile" style="background:var(--red)">
    <svg width="24" height="22" viewBox="0 0 24 22"><path d="M2 4h8c1 0 2 1 2 2v13c0-1-1-2-2-2H2zM22 4h-8c-1 0-2 1-2 2v13c0-1 1-2 2-2h8z" fill="#fff"/></svg>LESSON</div>
  <div class="side-tile" style="background:var(--purple)">
    <svg width="22" height="22" viewBox="0 0 22 22"><path d="M5 2h9l4 4v14H5z" fill="none" stroke="#fff" stroke-width="2"/><path d="M8 9h7M8 12h7M8 15h7" stroke="#fff" stroke-width="1.5"/></svg>BLOG</div>
  <div class="side-tile" style="background:var(--sky)">
    <svg width="22" height="22" viewBox="0 0 22 22"><rect x="3" y="10" width="9" height="5" rx="2.5" transform="rotate(-45 7.5 12.5)" fill="none" stroke="#fff" stroke-width="2"/><rect x="10" y="6" width="9" height="5" rx="2.5" transform="rotate(-45 14.5 8.5)" fill="none" stroke="#fff" stroke-width="2"/></svg>JOIN US</div>
  <div class="side-tile" style="background:var(--green)">
    <svg width="24" height="22" viewBox="0 0 24 22"><rect x="2" y="4" width="20" height="14" fill="none" stroke="#fff" stroke-width="1.6"/><path d="M2 4l10 8 10-8" fill="none" stroke="#fff" stroke-width="1.6"/></svg>CONTACT</div>
</div>

<div class="abs social" aria-label="Social network links">
  <div style="background:var(--navy)"></div>
  <div style="background:#2aaee0"></div>
  <div style="background:var(--red)"></div>
  <div style="background:#1d7fb8"></div>
  <div style="background:#cf3431"></div>
  <div style="background:var(--orange)"></div>
</div>

<section class="abs hero">
  <div class="hero-text">
    <h1>RAISING THE SKILL LEVELS OF STUDENTS IN HOME CONVENIENCE</h1>
    <p>Lorem ipsum dolor sit amet, consectetuer adipiscing elit, sed diam nonummy nibh euismod tincidunt ut.</p>
    <div class="more"><svg width="16" height="12" viewBox="0 0 16 12"><path d="M1 1l5 5-5 5M8 1l5 5-5 5" fill="none" stroke="#fff" stroke-width="2.2"/></svg>read more</div>
  </div>
  <div class="hero-photo" role="img" aria-label="Smiling teacher in a white coat in front of a chalkboard with formulas"></div>
</section>

<div class="abs cat-head">CATEGORIES</div>
<div class="abs cat-body"></div>

<div class="abs card" style="left:271px;top:462px;width:256px;height:86px;background:var(--navy)">
  <div class="card-photo" role="img" aria-label="Students raising hands in a classroom" style="background:linear-gradient(120deg,#2f4a5a,#7b8c95)"></div>
  <div class="card-text">Lorem ipsum dolor sit amet, consectetuer adipiscing elit.
    <div class="more"><svg width="16" height="12" viewBox="0 0 16 12"><path d="M1 1l5 5-5 5M8 1l5 5-5 5" fill="none" stroke="#fff" stroke-width="2.2"/></svg>read more</div></div>
</div>
<div class="abs card" style="left:271px;top:557px;width:256px;height:85px;background:var(--red)">
  <div class="card-photo" role="img" aria-label="Student working at a computer lab" style="background:linear-gradient(120deg,#e7e5e0,#9bc75a 70%,#3a2c28)"></div>
  <div class="card-text">Lorem ipsum dolor sit amet, consectetuer adipiscing elit.
    <div class="more"><svg width="16" height="12" viewBox="0 0 16 12"><path d="M1 1l5 5-5 5M8 1l5 5-5 5" fill="none" stroke="#fff" stroke-width="2.2"/></svg>read more</div></div>
</div>
<div class="abs feature">
  <div class="feature-photo" role="img" aria-label="Teacher helping children draw at a classroom table"></div>
  <p>Lorem ipsum dolor sit amet, consectetuer adipiscing elit.</p>
</div>

<div class="abs col-l">
  <div class="bar" style="background:var(--red)">EUROPE</div>
  <div class="bar" style="background:var(--sky)">ASIA</div>
  <div class="bar" style="background:var(--orange)">USA</div>
  <div class="bar" style="background:var(--green)">AUSTRALIA</div>
</div>
<div class="abs col-r">
  <div class="bar" style="background:var(--orange)">DRAMA</div>
  <div class="bar" style="background:var(--green)">SCIENCE</div>
  <div class="bar" style="background:var(--sky)">ENGLISH</div>
  <div class="bar" style="background:var(--red)">ARTS</div>
</div>

<aside class="abs articles">
  <div class="panel-head" style="background:var(--orange)">ARTICLES</div>
  <ul class="list">
    <li style="border-left-color:var(--green)">Ut viverra nibh sit amet eros luctus convallis.</li>
    <li style="border-left-color:var(--green)">Phasellus et libero at leo molestie dapibus.</li>
    <li style="border-left-color:var(--green)">Ut viverra nibh sit amet eros luctus convallis.</li>
    <li style="border-left-color:var(--purple)">Suspendisse dignissim sapien hendrerit mi</li>
    <li style="border-left-color:var(--orange)">Pellentesque, convallis tincidunt justo auctor.</li>
    <li style="border-left-color:var(--red)">Proin ut ligula egestas, tempus dui vel, sollicitudin leo.</li>
  </ul>
</aside>

<aside class="abs blogposts">
  <div class="panel-head" style="background:var(--sky)">BLOG POSTS</div>
  <ul class="list">
    <li style="border-left-color:var(--sky)">Ut viverra nibh sit amet eros luctus convallis.</li>
    <li style="border-left-color:var(--green)">Phasellus et libero at leo molestie dapibus.</li>
    <li style="border-left-color:var(--green)">Ut viverra nibh sit amet eros luctus convallis.</li>
    <li style="border-left-color:var(--navy)">Suspendisse dignissim sapien hendrerit mi</li>
    <li style="border-left-color:var(--sky)">Pellentesque, convallis tincidunt justo auctor.</li>
    <li style="border-left-color:var(--red)">Proin ut ligula egestas, tempus dui vel, sollicitudin leo.</li>
  </ul>
</aside>

<footer class="abs footer">
  <div class="fcol" style="width:178px;border-bottom-color:#2aaee0"><h3 style="color:#2aaee0">Quick Links</h3>
    <ul><li>Home</li><li>About Us</li><li>Support</li><li>Team</li><li>Contact Us</li></ul></div>
  <div class="fcol" style="width:187px;border-bottom-color:var(--orange);padding-left:42px"><h3 style="color:var(--orange)">Education</h3>
    <ul><li>Syllabus</li><li>Submit a Content</li><li>Consulting</li><li>Programs</li></ul></div>
  <div class="fcol" style="width:180px;border-bottom-color:#e22a7e;padding-left:42px"><h3 style="color:#e22a7e">Quick Links</h3>
    <ul><li>Home</li><li>About Us</li><li>Support</li><li>Team</li><li>Contact Us</li></ul></div>
  <div class="fcol" style="flex:1;border-bottom-color:#8cc63f;border-right:0;padding-left:42px"><h3 style="color:#8cc63f">Education</h3>
    <ul><li>Syllabus</li><li>Submit a Content</li><li>Consulting</li><li>Programs</li></ul></div>
</footer>

<div class="abs copy">Copyright © 2013 LumoraLearning. All rights reserved</div>

</body>
</html>
```